Wordpress Design Project

We are a Computer / Information Technology Company that will focus on the after-hours technical support for Home and Businesses.

I'm looking to have the home page as a static page with a links to blog, about us.

www.qmvolt.com.au is my web site.

Please do not chage uploaded logo's, do not copy current logo on website use uploaded files only, thanks.
Updates

Cheers

Derek

Target Market(s)

Home and Small office/home office, or SOHO Computer users.

Industry/Entity Type

Computer

Requirements
Should not have
• After hours tech support added to logo.

```html
<!DOCTYPE html>
<html lang="en">
<head>
<meta charset="utf-8">
<title>QM Volt – After hours tech support</title>
<link rel="stylesheet" href="https://fonts.googleapis.com/css2?family=Arimo:wght@400;700&family=PT+Sans:wght@400;700&family=Ubuntu:wght@500;700&display=swap">
<style>
:root{
  --navy:#0a2f78;
  --blue:#1c5fae;
  --sky:#0e9bd0;
  --menu:#0a9fd3;
  --ink:#222;
  --light:#f7f7f7;
  --rule:#c9c9c9;
  --panel:#d9d9d9;
  --heading:"PT Sans",sans-serif;
  --body:"Arimo",sans-serif;
}
*{margin:0;padding:0;box-sizing:border-box}
h1,h2,h4,h5{font-weight:400}
html,body{width:1200px;height:1114px;overflow:hidden;background:#fff;font-family:var(--body);color:var(--ink)}
.canvas{position:relative;width:1200px;height:1114px;overflow:hidden}
.abs{position:absolute}

.topline{left:0;top:0;width:1200px;height:5px;background:#e8e8e8}
.header{left:0;top:5px;width:1200px;height:98px;background:linear-gradient(#fff,#ececec)}
.brand{left:133px;top:33px;display:flex;align-items:center;gap:14px}
.brand-mark{width:44px;height:44px;border-radius:50%;background:var(--blue)}
.brand-name{font-family:var(--heading);font-weight:700;font-size:44px;color:var(--blue);line-height:1}

.nav{left:653px;top:44px;display:flex}
.nav a{display:block;height:29px;line-height:29px;padding:0 11px;font-family:var(--body);font-weight:700;font-size:11px;color:#666;text-decoration:none}
.nav a.active{background:var(--blue);color:#fff;border-radius:3px;padding:0 12px;margin-right:3px}
.nav a.open{background:#e6e6e6;color:var(--blue);border-radius:3px 3px 0 0;padding:0 12px;margin:0 4px 0 2px}

.hero{left:0;top:103px;width:1200px;height:224px;background:linear-gradient(#1b4f9e,#0b3a86 70%,#072a66)}
.hero-photo{left:126px;top:10px;width:290px;height:205px;background:linear-gradient(90deg,#8aa4c4,#c9a98a 45%,#2f65b0)}
.hero-fade{left:416px;top:10px;width:434px;height:205px;background:linear-gradient(90deg,#2d76c4,#1c5eb3 60%,#174e9f)}
.hero-title{left:430px;top:18px;width:410px;font-family:"Ubuntu",sans-serif;font-weight:700;font-size:23px;line-height:31px;color:#fff;letter-spacing:.3px}
.hero-copy{left:430px;top:120px;width:400px;font-size:12px;line-height:17.5px;color:#cfe0f5}
.dots{left:738px;top:198px;display:flex;gap:5px}
.dots span{width:12px;height:12px;border-radius:50%;background:#1a3f80}
.dots span:first-child{background:#3a64a8}

.submenu{left:851px;top:80px;width:130px;height:246px;background:var(--menu);border:1px solid #6cc8ea;padding:9px 4px}
.submenu a{display:block;height:34px;line-height:34px;padding-left:10px;font-size:10.5px;color:#fff;text-decoration:none}
.submenu a.current{height:30px;line-height:30px;background:#fff;color:var(--sky);border-radius:2px;margin-bottom:4px}

.intro{left:0;top:327px;width:1200px;height:94px;background:var(--light);border-bottom:1px solid #e2e2e2}
.intro-bar{left:121px;top:27px;width:4px;height:44px;background:#ccc}
.intro-title{left:143px;top:20px;font-family:var(--heading);font-size:26px;color:var(--sky)}
.intro-sub{left:143px;top:51px;font-family:var(--heading);font-size:19px;color:#999}
.tour{left:821px;top:35px;width:119px;height:32px;border-radius:3px;background:linear-gradient(#3b8fe0,#1c5eb3);box-shadow:0 8px 8px -6px rgba(0,0,0,.25);display:flex;align-items:center;gap:12px;padding-left:14px;font-family:var(--heading);font-size:14px;color:#fff}
.tour i{width:13px;height:13px;border-radius:50%;background:#6fb3f0}

.section-title{font-family:var(--heading);font-size:24px;color:var(--sky);border-bottom:1px solid var(--rule);line-height:1.1}
.welcome-title{left:139px;top:434px;width:388px}
.welcome-photo{left:133px;top:477px;width:198px;height:145px;border:4px solid #fff;outline:1px solid #ddd;background:linear-gradient(#3c4a5c,#7a5a60 60%,#38404c)}
.welcome-lead{left:341px;top:476px;width:270px;font-family:var(--heading);font-size:15px;line-height:17px;color:#222}
.services{left:348px;top:519px;list-style:none}
.services li{font-size:11px;color:#888;height:17.2px;line-height:17.2px;display:flex;align-items:center;gap:7px;letter-spacing:.3px}
.services li::before{content:"";width:9px;height:9px;border-radius:50%;background:#5cc9ef;border:2px solid #c7eefb}

.hours-title{left:136px;top:660px;width:389px;font-size:20px}
.hours-photo{left:130px;top:689px;width:218px;height:146px;border:4px solid #fff;outline:1px solid #ddd;background:linear-gradient(135deg,#dfe6ee,#a7b7c9 50%,#4a5f78)}
.hours{left:363px;top:696px;font-size:10px;font-weight:700;color:#666;line-height:20.6px}

.sidebar{left:827px;top:430px;width:200px;height:426px;background:var(--panel);border:2px solid #eee;padding:18px 19px}
.sidebar-head{display:flex;align-items:center;gap:8px;font-family:var(--heading);font-size:21px;color:var(--sky);margin-bottom:12px}
.sidebar-head i{width:22px;height:22px;border-radius:4px;background:#e8772e}
.sidebar h4{font-size:13px;color:#222;line-height:20.5px}
.sidebar a{display:block;font-size:12px;color:var(--sky);text-decoration:none;line-height:21px}
.sidebar a.small{font-size:11px;line-height:20.5px}
.sidebar-mark{left:22px;top:342px;font-family:var(--heading);font-weight:700;font-size:40px;color:#c6c6c6}

.qc-title{left:140px;top:866px;width:723px}
.qc-item{top:905px;width:150px}
.qc-icon{top:908px;width:26px;height:26px;border-radius:3px}
.qc-item h5{font-size:12px;font-weight:700;color:#333;letter-spacing:.3px;margin-bottom:3px}
.qc-item p{font-size:10.5px;line-height:17.5px;color:#888}
.qc-item a{font-size:9px;color:var(--blue);text-decoration:none}

.footer{left:0;top:1003px;width:1200px;height:111px;background:var(--navy)}
.footer-brand{left:154px;top:36px;display:flex;align-items:center;gap:12px}
.footer-brand i{width:36px;height:36px;border-radius:50%;background:#8ea8d0}
.footer-brand b{font-family:var(--heading);font-size:34px;color:#8ea8d0}
.social{left:484px;top:47px;display:flex;gap:10px}
.social span{width:20px;height:20px;border-radius:3px;background:#4d77b8}
.copyright{left:708px;top:55px;font-size:10.5px;color:#fff;letter-spacing:.3px}
</style>
</head>
<body>
<div class="canvas">
  <div class="abs topline"></div>
  <header class="abs header"></header>
  <div class="abs brand"><span class="brand-mark"></span><span class="brand-name">QM Volt</span></div>
  <nav class="abs nav">
    <a class="active">Home</a><a>About Us</a><a>Portfolio</a><a class="open">Pages</a><a>Blog</a><a>Contact</a>
  </nav>

  <section class="abs hero">
    <div class="abs hero-photo" role="img" aria-label="Support agent wearing a headset at a computer in an office"></div>
    <div class="abs hero-fade"></div>
    <h1 class="abs hero-title">After hours computer support for your convenience, with a no fix no fee policy.</h1>
    <p class="abs hero-copy">Lorem ipsum dolor sit amet, consectetuer adipiscing elit. Aenean commodo ligula eget dolor. Aenean massa. Cum sociis natoque penatibus et magnis dis parturient montes, nascetur ridiculus mus.</p>
    <div class="abs dots"><span></span><span></span><span></span><span></span><span></span></div>
  </section>

  <div class="abs submenu">
    <a class="current">With submenu</a><a>Full width</a><a>Header slider</a><a>Content slider</a><a>Result list</a><a>FAQ</a><a>Error page 404</a>
  </div>

  <section class="abs intro">
    <div class="abs intro-bar"></div>
    <h2 class="abs intro-title">Hello &amp; Welcome to QMVolt.com</h2>
    <p class="abs intro-sub">we are &nbsp;after hours tech support company</p>
    <div class="abs tour"><i></i>Take a Tour</div>
  </section>

  <h2 class="abs section-title welcome-title">Welcome</h2>
  <div class="abs welcome-photo" role="img" aria-label="Technicians standing in a server room"></div>
  <p class="abs welcome-lead">After hours computer support for your convenience, with a no fix no fee policy.</p>
  <ul class="abs services">
    <li>No job is too small Laptop or PC:</li>
    <li>Home ADSL.</li>
    <li>Wireless.</li>
    <li>Virus removal.</li>
    <li>Desktops configuration and installation.</li>
    <li>Laptop configuration and installation.</li>
    <li>Hardware.</li>
  </ul>

  <h2 class="abs section-title hours-title">After Hours Appointments Available</h2>
  <div class="abs hours-photo" role="img" aria-label="Handheld organiser and stylus resting on an appointment diary"></div>
  <div class="abs hours">
    Mon: 6:00 PM-9:00 PM<br>Tue: 6:00 PM-9:00 PM<br>Wed: 6:00 PM-9:00 PM<br>Thu: 6:00 PM-9:00 PM<br>Fri: 6:00 PM-9:00 PM<br>Sat: 10:00 AM-9:00 PM<br>Sun: 10:00 AM-9:00 PM
  </div>

  <aside class="abs sidebar">
    <div class="sidebar-head"><i></i>Blog</div>
    <h4>Recent Posts</h4>
    <a>Workstation imaging</a>
    <h4>Recent Comments</h4>
    <h4>Archives</h4>
    <a>September 2011</a>
    <h4>Categories</h4>
    <a class="small">Desktops</a>
    <h4>Meta</h4>
    <a class="small">Log in</a><a class="small">Entries RSS</a><a class="small">Comments RSS</a><a class="small">PressKit.org</a>
    <div class="abs sidebar-mark">QM Volt</div>
  </aside>

  <h2 class="abs section-title qc-title">Quick Contact</h2>
  <div class="abs qc-icon" style="left:143px;background:#c44" role="img" aria-label="Tools icon"></div>
  <div class="abs qc-item" style="left:188px"><h5>Help and support</h5><p>Vestibulum sit amet neque eu neque suscipit consequat quis vel risus.</p><a>continue reading »</a></div>
  <div class="abs qc-icon" style="left:358px;background:#3a7fc8" role="img" aria-label="Information book icon"></div>
  <div class="abs qc-item" style="left:402px"><h5>What we do</h5><p>Praesent fringilla, eros et tristique tempus, libero metus</p><a>continue reading »</a></div>
  <div class="abs qc-icon" style="left:561px;background:#9ab" role="img" aria-label="Magnifier icon"></div>
  <div class="abs qc-item" style="left:605px"><h5>Special event</h5><p>Curabitur blandit odio eget odio eleifend vel mattis augue convallis.</p><a>continue reading »</a></div>
  <div class="abs qc-icon" style="left:768px;background:#e9c95a" role="img" aria-label="Calendar icon"></div>
  <div class="abs qc-item" style="left:812px"><h5>Special package</h5><p>Ut dapibus est id odio pretium blandit in eget leo. Aliquam erat volutpat.</p><a>continue reading »</a></div>

  <footer class="abs footer">
    <div class="abs footer-brand"><i></i><b>QM Volt</b></div>
    <div class="abs social"><span></span><span></span><span></span><span></span><span></span><span style="background:#e8772e"></span></div>
    <p class="abs copyright">© Copyright 2012. &nbsp;QMVOLT.COM.AU, All Rights Reserved.</p>
  </footer>
</div>
</body>
</html>
```